I am a Financial Adviser specialising in Aged Care Advice. We provide financial advice and assistance to families with loved ones entering an Aged Care facility.
We need a flyer detailing the Aged Care Packages that we offer. There will be 3 main packages & then other add ons. I need an area where the client can sign off on the package/s that they choose. I have attached a sample to demonstrate the required layout, and a copy of content. I would like the flyer to have an image as per the attached sample, and to be designed in soft pastels, blues, greens.

Financial

```html
<!DOCTYPE html>
<html lang="en">
<head>
<meta charset="utf-8">
<title>Aged Care Services Flyer</title>
<link href="https://fonts.googleapis.com/css2?family=Montserrat:ital,wght@0,300;0,400;0,500;0,600;1,300;1,400&display=swap" rel="stylesheet">
<style>
:root{
  --bg:#3a3a3c;
  --paper:#ffffff;
  --ink:#2b2b2b;
  --body:#4a4a4a;
  --gold:#c9a94a;
  --green:#7fbf5f;
  --green-soft:#cfe8a8;
  --aqua:#d6eef3;
  --pink:#f2a6c9;
  --leaf:#78b963;
  --sky:#7ec9f0;
}
*{box-sizing:border-box;margin:0;padding:0}
html,body{width:1200px;height:1200px;overflow:hidden;background:var(--bg)}
body{font-family:"Montserrat",sans-serif;color:var(--body);position:relative}
.page{position:absolute;top:196px;width:630px;height:893px;background:var(--paper);transform:scale(.905);transform-origin:0 0;overflow:hidden}
.page--front{left:20px}
.page--back{left:610px}
.abs{position:absolute}
.backdrop{position:absolute;inset:0}
.photo{position:absolute}
.brand{left:52px;top:52px;font-size:17px;font-weight:500;color:var(--ink);display:flex;align-items:center;gap:8px;letter-spacing:.5px}
.brand-dot{width:11px;height:11px;border-radius:50%;background:var(--gold)}
.hero-title{left:46px;top:138px;font-size:43px;font-weight:500;line-height:1.12;color:var(--ink)}
.check{width:21px;height:19px;border:2px solid #333;border-radius:4px;background:#fff}
.pkg-name{font-size:17.5px;font-weight:400;color:var(--ink);line-height:1.1}
.pkg-tag{font-size:13px;font-style:italic;font-weight:400;color:var(--ink)}
.ribbon{left:398px;width:232px;height:31px;color:#fff;font-size:17px;font-style:italic;font-weight:400;padding:4px 0 0 20px}
.ribbon--pink{background:var(--pink)}
.ribbon--green{background:var(--leaf)}
.ribbon--blue{background:var(--sky)}
.list{list-style:none;font-size:11.6px;line-height:18px;font-weight:400;color:var(--body)}
.list li{position:relative;padding-left:15px}
.list li::before{content:"·";position:absolute;left:0}
.list .lead{padding-left:0;font-weight:600;color:var(--ink)}
.list .lead::before{content:""}
.list .lead i{font-weight:600}
.note{font-size:10.5px;font-style:italic;line-height:15px}
.extras-title{left:38px;top:36px;font-size:20px;font-weight:400;color:var(--ink);letter-spacing:.3px}
.option{left:36px;width:560px;display:flex;gap:19px}
.option-text{font-size:11.6px;line-height:15px;text-align:justify}
.option-text b{font-weight:600;color:var(--ink);display:block}
.sign-box{left:37px;top:563px;width:555px;height:160px;border:2px solid var(--gold);border-radius:8px;padding:10px 13px;font-size:10.4px;line-height:15px;text-align:justify}
.sig{position:absolute;width:95px;border-top:1px solid #555;text-align:center;font-size:10.4px;padding-top:3px}
.legal{left:37px;top:738px;width:555px;font-size:10.2px;line-height:15px;text-align:justify}
.legal b{font-weight:600;color:var(--ink)}
</style>
</head>
<body>

<!-- Front page: packages -->
<section class="page page--front">
  <svg class="backdrop" viewBox="0 0 630 893" width="630" height="893" aria-hidden="true">
    <defs>
      <linearGradient id="skyWash" x1="0" y1="0" x2="0.3" y2="1">
        <stop offset="0" stop-color="#d3eef4"/>
        <stop offset=".45" stop-color="#e9f5d8"/>
        <stop offset=".75" stop-color="#a9d676"/>
        <stop offset="1" stop-color="#6fb347"/>
      </linearGradient>
    </defs>
    <rect width="630" height="893" fill="url(#skyWash)"/>
  </svg>
  <div class="photo" role="img" aria-label="Photo of an elderly person's hands held gently by a younger hand" style="left:290px;top:0;width:340px;height:380px;background:radial-gradient(circle at 60% 45%,#c9b3a6,#8e7f78 60%,#6f6561)"></div>
  <svg class="backdrop" viewBox="0 0 630 893" width="630" height="893" aria-hidden="true">
    <ellipse cx="345" cy="650" rx="400" ry="350" fill="#fff"/>
    <path d="M-20 420 Q120 300 330 292 Q520 290 640 360" fill="none" stroke="var(--gold)" stroke-width="3"/>
    <path d="M0 690 Q40 860 250 893" fill="none" stroke="#b9dd95" stroke-width="3"/>
  </svg>

  <div class="abs brand"><span class="brand-dot"></span>Evergreen Wealth</div>
  <h1 class="abs hero-title">Aged Care<br>Services</h1>

  <div class="abs check" style="left:40px;top:365px"></div>
  <div class="abs" style="left:88px;top:357px"><div class="pkg-name">ESSENTIALS Package $770</div><div class="pkg-tag">When you know what you want</div></div>
  <div class="abs ribbon ribbon--pink" style="top:360px">Peace of Mind</div>
  <ul class="abs list" style="left:50px;top:406px;width:260px;text-align:justify">
    <li>Explanation of Aged Care Fees and Charges.</li>
    <li>Preliminary Home/Assets Assessment.*</li>
    <li>Estimated Means Tested Fee Calculation.*</li>
    <li>Preliminary Aged Care Costs.*</li>
  </ul>
  <ul class="abs list" style="left:329px;top:406px;width:260px"><li>Estimated Cash Flow Scenario.*</li></ul>
  <p class="abs note" style="left:343px;top:442px;width:245px">*Please note this is general factual information only. We do not provide any specific personal information.</p>

  <div class="abs check" style="left:40px;top:543px"></div>
  <div class="abs" style="left:88px;top:535px"><div class="pkg-name">ADVANTAGE Package $2,970</div><div class="pkg-tag">When you need to know the options</div></div>
  <div class="abs ribbon ribbon--green" style="top:537px">Confidence</div>
  <ul class="abs list" style="left:50px;top:583px;width:260px">
    <li class="lead">ESSENTIALS Package <i>plus</i></li>
    <li>Analyse and Strategize Aged Care costs.</li>
    <li>Compare up to 5 Strategy options.</li>
    <li>Minimise Aged Care Costs (where possible).</li>
  </ul>
  <ul class="abs list" style="left:329px;top:583px;width:260px;text-align:justify">
    <li>Maximise Age Pension Income (where possible).</li>
    <li>Prepare a Full Statement of Advice (SOA).</li>
    <li>Implementation of Aged Care Strategy.</li>
  </ul>

  <div class="abs check" style="left:40px;top:708px"></div>
  <div class="abs" style="left:88px;top:700px"><div class="pkg-name">PLATINUM Package $5,940</div><div class="pkg-tag">When you need someone to take charge</div></div>
  <div class="abs ribbon ribbon--blue" style="top:701px">Convenience</div>
  <ul class="abs list" style="left:50px;top:749px;width:260px">
    <li class="lead">ESSENTIALS Package <i>plus</i></li>
    <li>Liase with the Aged Care Facility</li>
    <li>CentreLink/DVA Nominee.</li>
  </ul>
  <ul class="abs list" style="left:329px;top:749px;width:260px">
    <li>Post Entry Review.</li>
    <li>Post Implementation SOA (if required).</li>
    <li>Annual Review.</li>
  </ul>
</section>

<!-- Back page: extra options -->
<section class="page page--back">
  <svg class="backdrop" viewBox="0 0 630 893" width="630" height="893" aria-hidden="true">
    <defs>
      <linearGradient id="topWash" x1="0" y1="0" x2="1" y2="0">
        <stop offset="0" stop-color="#c4e39b"/>
        <stop offset=".5" stop-color="#eef7e1"/>
        <stop offset="1" stop-color="#ffffff"/>
      </linearGradient>
    </defs>
    <path d="M0 0 H630 V120 Q330 70 0 100 Z" fill="url(#topWash)"/>
    <path d="M0 100 Q300 75 560 95" fill="none" stroke="#e1efd0" stroke-width="6"/>
  </svg>
  <div class="photo" role="img" aria-label="Photo of a smiling multi-generation family sitting together on grass" style="left:308px;top:-20px;width:330px;height:310px;border-radius:0 0 0 60%;background:radial-gradient(circle at 50% 40%,#d9dfcf,#9fb77a 55%,#6e9a45);border-bottom:4px solid var(--gold)"></div>

  <h2 class="abs extras-title">EXTRA CHOICE OPTIONS</h2>

  <div class="abs option" style="top:100px;width:300px"><div class="check"></div><p class="option-text" style="width:232px"><b>CentreLink/DVA Nominee $1,100</b>Communicate with CentreLink/DVA on behalf of our client/s, and undertake all changes and updates to details, as directed by our client.</p></div>
  <div class="abs option" style="top:185px;width:340px"><div class="check"></div><p class="option-text" style="width:290px"><b>Post Implementation<br>Statement of Advice $1,650</b>Revise our original Advice Statement for any changes of circumstances including income &amp; asset variations, and provide further advice within the first 12 months of initial advice statement.</p></div>
  <div class="abs option" style="top:286px"><div class="check"></div><p class="option-text"><b>Annual Review $990</b>Communicate with CentreLink/DVA on behalf of our client/s, and undertake all changes and updates to details, as directed by our client.</p></div>
  <div class="abs option" style="top:341px"><div class="check"></div><p class="option-text"><b>Post Entry Review $660</b>Review financial situation, check facility invoices are accurate, explain the Residential Aged Care Agreement and ensure all recommendations are implemented.</p></div>
  <div class="abs option" style="top:397px"><div class="check"></div><p class="option-text"><b>Facility Liason $550</b>Negotiate with the Aged Care Facility regarding Accommodation payments, clarify &amp; explain Residential Care Agreement, and review facility invoices.</p></div>
  <div class="abs option" style="top:452px"><div class="check"></div><p class="option-text"><b>Family Conferences $660</b>Facilitate &amp; co-ordinate family meetings to explain the Aged Care legislation and how it fits with the family circumstances.</p></div>
  <div class="abs option" style="top:508px"><div class="check"></div><p class="option-text"><b>Tick Box &nbsp; Estate Wrap $660</b>Assist beneficiaries with correct procedures and paperwork regarding the finalisation of the estate.</p></div>

  <div class="abs sign-box">
    <p>I/We have chosen the Service Package and Options as ticked above. I/We understand that by choosing the Essentials Package, that I/We are receiving factual information only, and not financial advice. I/We agree to pay the amount of ____________ , within seven days of the date of the invoice received from Evergreen Wealth SA.</p>
    <div class="sig" style="left:38px;top:90px">Signature</div>
    <div class="sig" style="left:167px;top:90px">Signature</div>
    <div class="sig" style="left:296px;top:90px">Signature</div>
    <div class="sig" style="left:420px;top:90px">Date</div>
    <div class="sig" style="left:38px;top:129px">Adviser Signature</div>
    <div class="sig" style="left:167px;top:129px">Date</div>
    <span class="abs" style="left:450px;top:72px">/ &nbsp; &nbsp; /</span>
    <span class="abs" style="left:197px;top:112px">/ &nbsp; &nbsp; /</span>
  </div>

  <div class="abs legal">
    <p><b>Important Information</b><br>This document has been prepared by Evergreen Wealth SA Pty Ltd ABN 12 345 678 901, an Authorised Representative of Northbridge Advice Limited ABN 98 765 432 109 AFSL 123456, a wholly owned, non-guaranteed subsidiary of the Harbour National Bank ABN 11 222 333 444.</p>
    <p style="margin-top:15px">Information in this document is based on current regulatory requirements and laws, as at 20 September, 2016 which may be subject to change. It contains general advice. It does not take into account your individual objectives, financial situation or needs. You should consider talking to a financial adviser before making a financial decision.</p>
  </div>
</section>

</body>
</html>
```